Mexican construction company needs a business card design

We need a business card design for a company based in Monterrey, Mexico called:

Desarrollos Tolvani S.A. de C.V.

The company is in the construction business and I would like the businees card to be simple and concise. Please use white background and blue or black text color that say:

"Proyectos de Construcción"-- (Brief description of business)
" Rodrigo Ulloa Benítez"--- (My name)
"rulloab@correovelo.mx"-- (My email)
"C: (81) 82 19 57 46"-- (My cell)
"O: (81) 86 72 13 95"-- (Office phone)

Please use only the colors of my company that are attached

Please make the back of the business card blue (same blue from logo) and use the logo.

Thanks!

```html
<!DOCTYPE html>
<html lang="es">
<head>
<meta charset="utf-8">
<title>Desarrollos Tolvani — Tarjeta de presentación</title>
<link rel="stylesheet" href="https://fonts.googleapis.com/css2?family=Arimo:wght@400;700&display=swap">
<style>
  :root {
    --navy: #0b0b47;
    --grey: #9b9b9b;
    --paper: #ffffff;
    --edge: #d6d6d6;
    --ink: #1a1a1a;
  }
  * { margin: 0; padding: 0; box-sizing: border-box; }
  html, body { width: 1169px; height: 1200px; overflow: hidden; background: var(--paper); }
  body { position: relative; font-family: "Arimo", Arial, sans-serif; color: var(--ink); }

  .side-label {
    position: absolute; left: 272px; width: 744px; text-align: center;
    font-size: 30px; font-weight: 400; color: var(--ink);
  }
  .side-label--front { top: 140px; }
  .side-label--back { top: 625px; }

  .card { position: absolute; left: 272px; width: 744px; height: 403px; overflow: hidden; }
  .card--front { top: 199px; background: var(--paper); border: 1px solid var(--edge); }
  .card--back { top: 683px; background: var(--navy); }

  .company-title {
    position: absolute; top: 14px; left: 0; width: 100%; text-align: center;
    font-size: 35px; font-weight: 700; letter-spacing: 2.5px; color: var(--navy);
  }
  .edge-bar { position: absolute; right: 0; top: 70px; width: 24px; height: 257px; background: var(--navy); }
  .edge-tab { position: absolute; left: -1px; top: 134px; width: 24px; height: 134px; background: var(--navy); border-radius: 0 14px 14px 0; }

  .brand {
    position: absolute; display: flex; align-items: center;
    font-weight: 700; color: var(--navy);
  }
  .brand__square { display: inline-block; background: var(--grey); }
  .brand--front { left: 110px; top: 150px; gap: 12px; font-size: 40px; }
  .brand--front .brand__square { width: 30px; height: 30px; }

  .tagline { position: absolute; left: 64px; top: 282px; font-size: 19px; color: var(--grey); }

  .holder-name { position: absolute; left: 422px; top: 176px; font-size: 23px; color: var(--navy); }

  .contact-list { position: absolute; left: 422px; top: 308px; list-style: none; font-size: 16px; line-height: 23px; color: var(--navy); letter-spacing: 0.5px; }

  .brand--back { left: 0; top: 0; width: 100%; height: 100%; justify-content: center; gap: 28px; font-size: 96px; color: var(--paper); }
  .brand--back .brand__square { width: 70px; height: 70px; }
</style>
</head>
<body>
  <p class="side-label side-label--front">Front</p>
  <section class="card card--front" aria-label="Frente de la tarjeta">
    <h1 class="company-title">Desarrollos Tolvani S.A. de C.V.</h1>
    <div class="edge-tab"></div>
    <div class="edge-bar"></div>
    <div class="brand brand--front"><span class="brand__square"></span><span>Tolvani</span></div>
    <p class="tagline">Proyectos de Construcción</p>
    <p class="holder-name">Rodrigo Ulloa Benítez</p>
    <ul class="contact-list">
      <li>C : (81) 82 19 57 46</li>
      <li>O : (81) 86 72 13 95</li>
      <li>E : rulloab@correovelo.mx</li>
    </ul>
  </section>

  <p class="side-label side-label--back">Back</p>
  <section class="card card--back" aria-label="Reverso de la tarjeta">
    <div class="brand brand--back"><span class="brand__square"></span><span>Tolvani</span></div>
  </section>
</body>
</html>
```